Golf simulator membership club

I need a clean design that associates golf, golfclub, golf simulator. Currently building a golf simulator centre. I need link buttons on top and a short description of the concept on the front page. i have removed the details about booking. Will link to external booking. Maybe also news blog on the right side of the page. Must be responsive to work on PC, iPad, tabs and mobile phone. I have been recommended to ask for WordPress
Industry/Entity Type
Club
Number of Pages Required
1 page
Font styles to use
Sans Serif
Requirements
Must have
- Booking plugin as stated in main description. I have a logo that i have attached.
- Also need a contact form and "meld deg på" form like the one found on my existing homepage tindrift.no

```html
<!DOCTYPE html>
<html lang="no">
<head>
<meta charset="utf-8">
<title>Tindrift – Golf simulatorklubb</title>
<link href="https://fonts.googleapis.com/css2?family=Open+Sans:wght@400;600;700;800&display=swap" rel="stylesheet">
<style>
  :root {
    --green: #2a7a55;
    --green-dark: #1f6b47;
    --text: #333333;
    --muted: #555555;
    --panel: #f2f2f2;
    --rule: #e2e2e2;
    --footer: #333333;
    --white: #ffffff;
  }
  * { margin: 0; padding: 0; box-sizing: border-box; }
  html, body { width: 704px; height: 1200px; overflow: hidden; }
  body { font-family: "Open Sans", sans-serif; color: var(--text); background: var(--white); position: relative; }

  .hero { position: absolute; left: 0; top: 0; width: 704px; height: 386px;
    background: linear-gradient(180deg, #e6ecd2 0%, #b3c083 22%, #7b8f4e 42%, #6f9244 60%, #7ea24b 78%, #5f8434 100%); }
  .brand { position: absolute; left: 44px; top: 31px; display: flex; align-items: center; gap: 8px;
    font-weight: 700; font-size: 17px; color: var(--green-dark); }
  .brand-dot { width: 18px; height: 18px; border-radius: 50%; background: var(--green-dark); }
  .main-nav { position: absolute; top: 27px; left: 274px; display: flex; align-items: center; }
  .main-nav a { font-size: 8.6px; font-weight: 700; color: #111; text-decoration: none; text-transform: uppercase; margin-right: 22px; white-space: nowrap; }
  .main-nav a:last-child { margin-right: 0; }
  .main-nav a.active { background: var(--green-dark); color: var(--white); padding: 10px 10px; width: 75px; text-align: center; margin-right: 15px; }
  .hero-title { position: absolute; top: 158px; width: 100%; text-align: center; color: var(--white);
    font-weight: 800; font-size: 42px; letter-spacing: 2px; }
  .hero-sub { position: absolute; top: 208px; left: 130px; width: 444px; text-align: center; color: var(--white);
    font-weight: 800; font-size: 23px; line-height: 27px; }
  .hero-dots { position: absolute; top: 365px; left: 335px; display: flex; gap: 5px; }
  .hero-dots span { width: 5px; height: 5px; border-radius: 50%; background: var(--white); }
  .hero-dots span.on { background: var(--green); }

  .main-col { position: absolute; left: 44px; top: 415px; width: 406px; }
  .side-col { position: absolute; left: 466px; top: 415px; width: 195px; }

  .section-title { display: flex; align-items: center; gap: 12px; font-size: 15.4px; font-weight: 700;
    text-transform: uppercase; letter-spacing: .3px; color: var(--text); line-height: 22px; }
  .title-mark { width: 17px; height: 17px; border-radius: 50%; background: var(--green-dark); flex: none; }
  .feature-image { margin-top: 16px; height: 108px; background: radial-gradient(circle at 40% 45%, #f4f6ef 0 10%, #b5d060 28%, #6a9a2c 65%, #3d6d1d 100%); }
  .intro { margin-top: 14px; font-size: 9.3px; line-height: 15.2px; color: var(--muted); }
  .intro p { margin-bottom: 4px; }
  .btn { display: inline-block; background: var(--green); color: var(--white); font-size: 9px; font-weight: 700;
    text-transform: uppercase; text-decoration: none; padding: 9px 21px; letter-spacing: .3px; }
  .main-col .btn { margin-top: 20px; width: 97px; text-align: center; padding: 9px 0; }
  .divider { height: 1px; background: var(--rule); margin: 17px 0 12px; }
  .steps { list-style: none; margin-top: 12px; }
  .steps li { display: flex; align-items: center; font-size: 9px; line-height: 15.2px; color: var(--muted); margin-bottom: 9px; }
  .steps li span.txt { max-width: 352px; }
  .step-icon { width: 29px; height: 29px; border: 2px solid var(--green); border-radius: 50%; flex: none; margin-right: 15px;
    display: flex; align-items: center; justify-content: center; }

  .booking-card { height: 147px; background: linear-gradient(180deg, #0d0d0d 0%, #1c2414 55%, #4d6a2a 100%);
    text-align: center; color: var(--white); padding-top: 22px; }
  .booking-card h2 { font-size: 16px; font-weight: 700; line-height: 20.5px; letter-spacing: .5px; }
  .booking-card .btn { margin-top: 12px; width: 96px; padding: 9px 0; }
  .panel { background: var(--panel); padding: 12px 13px 12px; margin-top: 14px; }
  .post { display: flex; gap: 12px; padding: 8px 0 9px; border-bottom: 1px solid var(--rule); }
  .post:last-of-type { border-bottom: 0; }
  .post-thumb { width: 41px; height: 38px; flex: none; background: linear-gradient(135deg, #5b6f84, #27313a); }
  .post h3 { font-size: 10.2px; color: var(--green); font-weight: 600; line-height: 14px; }
  .post p, .news-item p { font-size: 8.4px; line-height: 13.5px; color: var(--text); }
  .panel p.more, .more { color: var(--green); }
  .panel .btn { margin-top: 6px; width: 97px; text-align: center; padding: 9px 0; }
  .news-item { padding: 7px 0 6px; border-bottom: 1px solid var(--rule); }
  .news-item:first-of-type { padding-top: 6px; }
  .news-item:last-of-type { border-bottom: 0; }
  .news-item time { font-size: 8.8px; font-weight: 700; color: var(--green); display: block; margin-bottom: 1px; }

  .site-footer { position: absolute; left: 0; top: 1074px; width: 704px; height: 126px; background: var(--footer);
    text-align: center; color: var(--white); }
  .footer-nav { margin-top: 24px; font-size: 9.6px; }
  .footer-nav span { margin: 0 7px; }
  .social { display: flex; justify-content: center; gap: 12px; margin-top: 14px; }
  .social span { width: 11px; height: 11px; border-radius: 50%; background: var(--white); }
  .copyright { margin-top: 13px; font-size: 6.8px; line-height: 13px; color: #aaaaaa; }
</style>
</head>
<body>
  <header class="hero" role="img" aria-label="Golfer putting on a sunlit fairway with trees and hills">
    <div class="brand"><span class="brand-dot"></span>tindrift.no</div>
    <nav class="main-nav">
      <a class="active" href="#">Startsiden</a>
      <a href="#">Meld deg på nå</a>
      <a href="#">Booking</a>
      <a href="#">Nyheter</a>
      <a href="#">Kontakt oss</a>
    </nav>
    <h1 class="hero-title">TINDRIFT</h1>
    <p class="hero-sub">We are a golf club &amp; are creating a golf simulator club</p>
    <div class="hero-dots"><span class="on"></span><span></span><span></span><span></span></div>
  </header>

  <main class="main-col">
    <h2 class="section-title"><span class="title-mark"></span>Døgnåpen golf simulatorklubb</h2>
    <div class="feature-image" role="img" aria-label="Golf ball on a tee beside a driver on green grass"></div>
    <div class="intro">
      <p>Snart åpner Norges første golfsimulatorklubb på Solvik! Kun kr. 750,- per mnd for<br>medlemskap med ubegrenset spilletid.</p>
      <p>Vi ønsker å lage en golf simulator klubb for trivsel og aktivitet på Bekkely. Vi har foreløpig plass<br>til 6 simulatorer.</p>
      <p>Vi bygger ut med ny simulator for hvert 15. medlem så her er det førstemann til mølla.<br>Medlemsprisen pr.mnd tilsvarer noe over 2 timer spill på andre simulatorsenter i Norge.<br>Den lave prisen forutsetter at vi har kontinuitet i medlemsmassen og vi har årsforfall på<br>medlemskapet 1. Desember. Dvs at man tegner seg for et år om gangen slik som i golfklubben.<br>(Noe kortere dette oppstartsåret)</p>
    </div>
    <a class="btn" href="#">Read more</a>
    <div class="divider"></div>
    <h2 class="section-title"><span class="title-mark"></span>Slik er prosessen</h2>
    <ol class="steps">
      <li><span class="step-icon"><svg width="10" height="11" viewBox="0 0 10 11"><path d="M1 0h5l3 3v8H1z" fill="#333"/></svg></span><span class="txt">Your interest on the site via the contact form, not binding!</span></li>
      <li><span class="step-icon"><svg width="11" height="8" viewBox="0 0 11 8"><rect width="11" height="8" fill="#333"/><path d="M0 0l5.5 4L11 0" stroke="#fff" fill="none"/></svg></span><span class="txt">We send a contract by email to you, you sign and return to us.</span></li>
      <li><span class="step-icon"><svg width="12" height="8" viewBox="0 0 12 8"><rect x=".5" y=".5" width="11" height="7" fill="none" stroke="#333"/><circle cx="6" cy="4" r="2" fill="#333"/></svg></span><span class="txt">You pay one enrollment fee of 500, - and the first month membership fee. This will take place one week before the simulator is ready to play. This is to prepare user profile and code / code chip for access to the center.</span></li>
      <li><span class="step-icon"><svg width="10" height="11" viewBox="0 0 10 11"><path d="M1 0h5l3 3v8H1z" fill="#333"/></svg></span><span class="txt">You will receive a code / code chip to the center and can start booking of hours on any free simulator center via booking app and / or website.</span></li>
      <li><span class="step-icon"><svg width="10" height="10" viewBox="0 0 10 10"><rect y="1" width="10" height="9" fill="#333"/><path d="M1 4h8M1 6h8M1 8h8M3.5 3v7M6.5 3v7" stroke="#fff" stroke-width=".6"/></svg></span><span class="txt">The center is open 24/7/365 and only rarely staffed</span></li>
    </ol>
  </main>

  <aside class="side-col">
    <section class="booking-card" role="img" aria-label="Dark golf simulator scene with golf balls">
      <h2>HOURLY BOOKINGS<br>FOR 24/7/365<br>ON 6 SIMULATORS</h2>
      <a class="btn" href="#">Book now</a>
    </section>

    <section class="panel">
      <h2 class="section-title"><span class="title-mark"></span>Blog posts</h2>
      <article class="post">
        <div class="post-thumb" role="img" aria-label="Simulator room"></div>
        <div><h3>Lorem ipsum dolor</h3><p>Vestibulum ante ipsum primis in faucibus...<span class="more">Read More</span></p></div>
      </article>
      <article class="post">
        <div class="post-thumb" role="img" aria-label="Simulator screen"></div>
        <div><h3>Lorem ipsum dolor</h3><p>Vestibulum ante ipsum primis in faucibus...<span class="more">Read More</span></p></div>
      </article>
      <a class="btn" href="#">Read all</a>
    </section>

    <section class="panel">
      <h2 class="section-title"><span class="title-mark"></span>Latest news</h2>
      <div class="news-item"><time>JAN 23, 2017</time><p>Se presentasjon av software og hardware..</p><p class="more">Read More</p></div>
      <div class="news-item"><time>JAN 23, 2017</time><p>Se presentasjon av software og hardware..</p><p class="more">Read More</p></div>
      <div class="news-item"><time>JAN 23, 2017</time><p>Se presentasjon av software og hardware..</p><p class="more">Read More</p></div>
      <a class="btn" href="#">Read all</a>
    </section>
  </aside>

  <footer class="site-footer">
    <nav class="footer-nav">Startsiden<span>/</span>Booking<span>/</span>Nyheter<span>/</span>Kontakt oss</nav>
    <div class="social"><span></span><span></span><span></span><span></span><span></span></div>
    <p class="copyright">Copyright © 2017 Company Name.<br>All Right Reserved</p>
  </footer>
</body>
</html>
```